Design for Perch Lane real estate agency

Incorporate logo into new business cards. I need to include the Marlowe Ridge logo incorporated into Perch Lane on one side of the card (attached). On the other side I see just the icon with "Tessa Lorne" (attached) with "Rooted in Care" either included as is or removed from logo and rather put as a tag line on the business card separate from the main logo. Contact information:

Tessa Lorne
Associate Broker
Cell: 914-555-0173
Email: tessalorne@perchlane.example
Web: www.perchlane.example

Target Market(s)

Buyers, Sellers, Builders and Investors of homes and land

Industry/Entity Type

Real Estate Agent

Contact Information for Business Card

My client base tend to be higher end home buyers, sellers, builders and investors. I have been more and more in land and subdivisions for builders and investors. The card should not be cluttered. Clean and simple - yet with an air of exclusive/high end

Colors

Designer to choose colors to be used in the design.

Requirements
Must have
• Must have the logo on one side that has Marlowe Ridge logo incorporated. The side that has my contact information does not have to have the Marlowe Ridge logo incorporated.
• Must include "Rooted in Care" tag line either within logo (as is) or removed from logo and included in another position on the side of the business card with contact information.
Should not have
• Should not have Marlowe Ridge logo incorporated into Perch Lane logo on both sides of business card. Would like the Perch Lane logo that has Marlowe Logo only on the back side of card without contact information.

```html
<!DOCTYPE html>
<html lang="en">
<head>
<meta charset="utf-8">
<title>Perch Lane – Business Card</title>
<link href="https://fonts.googleapis.com/css2?family=Lora:wght@400;600&display=swap" rel="stylesheet">
<style>
  :root {
    --backdrop: #3b322e;
    --card: #121212;
    --card-edge: #1c1c1c;
    --gold: #c99a2e;
    --gold-soft: #a88232;
    --emboss: #3a3a3a;
  }
  * { box-sizing: border-box; margin: 0; padding: 0; }
  html, body { width: 1200px; height: 716px; overflow: hidden; }
  body {
    background: var(--backdrop);
    font-family: "Lora", Georgia, serif;
    position: relative;
  }
  .card {
    position: absolute;
    top: 208px;
    width: 520px;
    height: 300px;
    background: var(--card);
    border: 1px solid var(--card-edge);
    border-radius: 3px;
    box-shadow: 0 14px 30px rgba(0,0,0,0.45);
  }
  .card--back { left: 50px; }
  .card--front { left: 630px; }

  /* back side: mark replaced by name */
  .back-mark {
    position: absolute;
    inset: 0;
    display: flex;
    align-items: center;
    justify-content: center;
    color: var(--emboss);
    font-size: 46px;
    font-weight: 600;
    letter-spacing: 1px;
  }

  /* front side: logo lockup */
  .lockup {
    position: absolute;
    top: 62px;
    right: 34px;
    text-align: right;
    color: var(--gold);
  }
  .lockup__name {
    font-size: 34px;
    font-weight: 600;
    line-height: 1;
  }
  .lockup__rule {
    height: 1px;
    background: var(--gold);
    margin: 8px 0 5px 40px;
  }
  .lockup__agent {
    display: flex;
    justify-content: flex-end;
    align-items: center;
    gap: 8px;
  }
  .lockup__lines { text-align: right; }
  .lockup__agent-name {
    font-size: 11px;
    letter-spacing: 3px;
    font-weight: 600;
  }
  .lockup__tagline {
    font-size: 6px;
    letter-spacing: 2px;
    color: var(--gold-soft);
  }
  .partner-badge {
    width: 30px;
    height: 20px;
    background: var(--gold);
  }

  /* front side: contact block */
  .contact {
    position: absolute;
    left: 32px;
    bottom: 42px;
    color: var(--gold);
  }
  .contact__name {
    font-size: 19px;
    font-weight: 600;
    letter-spacing: 0.5px;
  }
  .contact__title {
    font-size: 11px;
    color: var(--gold-soft);
    margin-bottom: 8px;
  }
  .contact__row {
    display: flex;
    align-items: center;
    gap: 8px;
    font-size: 13px;
    line-height: 19px;
  }
  .contact__icon { width: 11px; height: 11px; flex: none; }
  .contact__row--plain { padding-left: 0; }
</style>
</head>
<body>
  <section class="card card--back" aria-label="Card back">
    <div class="back-mark">Perch Lane</div>
  </section>

  <section class="card card--front" aria-label="Card front">
    <div class="lockup">
      <div class="lockup__name">Perch Lane</div>
      <div class="lockup__rule"></div>
      <div class="lockup__agent">
        <div class="lockup__lines">
          <div class="lockup__agent-name">TESSA LORNE</div>
          <div class="lockup__tagline">ROOTED IN CARE</div>
        </div>
        <div class="partner-badge" role="img" aria-label="Marlowe Ridge partner badge"></div>
      </div>
    </div>

    <div class="contact">
      <div class="contact__name">TESSA LORNE</div>
      <div class="contact__title">Associate Broker</div>
      <div class="contact__row">
        <svg class="contact__icon" viewBox="0 0 12 12" aria-hidden="true"><rect width="12" height="12" rx="2" fill="#c99a2e"/><path d="M3.5 3 L5 3 L5.6 4.6 L4.8 5.3 Q5.6 6.8 6.8 7.3 L7.5 6.5 L9 7.1 L9 8.6 Q5 9 3.4 4.6 Z" fill="#121212"/></svg>
        <span>914-555-0173</span>
      </div>
      <div class="contact__row">
        <svg class="contact__icon" viewBox="0 0 12 12" aria-hidden="true"><rect width="12" height="12" rx="2" fill="#c99a2e"/><rect x="2.5" y="3.5" width="7" height="5" fill="none" stroke="#121212"/><path d="M2.5 3.5 L6 6.3 L9.5 3.5" fill="none" stroke="#121212"/></svg>
        <span>tessalorne@perchlane.example</span>
      </div>
      <div class="contact__row">
        <svg class="contact__icon" viewBox="0 0 12 12" aria-hidden="true"><circle cx="6" cy="6" r="6" fill="#c99a2e"/><circle cx="6" cy="6" r="3.5" fill="none" stroke="#121212"/><path d="M2.5 6 H9.5 M6 2.5 V9.5" stroke="#121212"/></svg>
        <span>www.perchlane.example</span>
      </div>
    </div>
  </section>
</body>
</html>
```